German Webagency needs fresh modern Design

Our website is 4 years old. We need an fresh modern website. All pics we used before are from customers or handmade by us. the new website should be clear with nice handling. please dont copy something from template websites. it would be great if you can surprise us with something great. its our first project here. don´t worry if i make a mistake in responding or briefing. after 20 years you can´t see the works of your own "designer" so we hope for help :-)
our existing site: www.tovankreativ.de
Target Market(s)
small and middle sized companys in germany
Number of Pages Required
4 page
Font styles to use
Colors
Designer to choose colors to be used in the design.
Requirements
Must have
- Responsive (sure we code it)
- Modern and big Font ..Headlines and Slider
- innovative..if you know something new..feel free to show
Nice to have
- the site with our works/refences should look great and later easy to handle when we code it or use wp.
- we like black and grey but if you have better ideas also feel free
Should not have
- a cup of coffe..laptop.. a pencil a handwritten font
- dont copy and modify templates from know websites..bad style

```html
<!DOCTYPE html>
<html lang="de">
<head>
<meta charset="utf-8">
<title>TovanKreativ.de – Ideen &amp; Visionen</title>
<link href="https://fonts.googleapis.com/css2?family=Poppins:wght@400;500;600;700&family=PT+Sans:wght@400;700&display=swap" rel="stylesheet">
<style>
:root{
  --purple:#3e1f66;
  --purple-deep:#2c1450;
  --purple-soft:#55327f;
  --ink:#1d1d1f;
  --text:#555;
  --muted:#8a8a8a;
  --band:#e6eaf0;
  --white:#fff;
}
*{margin:0;padding:0;box-sizing:border-box}
html,body{width:1200px;height:3529px;overflow:hidden;background:var(--white)}
body{position:relative;font-family:"PT Sans",sans-serif;color:var(--text)}
.abs{position:absolute}
.heading{font-family:"Poppins",sans-serif;font-weight:500;color:var(--ink);text-transform:uppercase;text-align:center;font-size:28px;letter-spacing:.5px}
.btn{position:absolute;display:flex;align-items:center;justify-content:center;font-family:"PT Sans",sans-serif;font-size:15px;color:var(--white);background:var(--purple-deep)}
.bg-shape{position:absolute;left:0;top:0}

/* header */
.logo{font-family:"Poppins",sans-serif;font-weight:700;font-size:34px;color:var(--white);left:165px;top:30px}
.nav{left:552px;top:46px;display:flex;gap:22px;font-family:"Poppins",sans-serif;font-size:13px;font-weight:500;color:var(--white)}
.nav span.active{border-bottom:2px solid var(--white);padding-bottom:4px}

/* hero */
.hero-title{left:160px;top:205px;font-family:"Poppins",sans-serif;font-weight:600;font-size:54px;line-height:66px;color:var(--white)}
.hero-sub{left:160px;top:450px;font-size:18px;color:#e6ddf2}
.hero-btn{left:160px;top:520px;width:158px;height:50px;background:transparent;border:2px solid var(--white);font-size:16px}
.device{left:743px;top:155px;width:292px;height:497px;border-radius:22px;background:#111;padding:60px 14px}
.device-screen{width:100%;height:100%;background:radial-gradient(circle at 50% 45%,#8b6bd0 0,#5fb3e5 28%,#f4f4f6 55%)}

/* services */
.services-title{left:0;width:1200px;top:866px}
.services-desc{left:330px;width:540px;top:920px;text-align:center;font-size:12px;line-height:18px;color:var(--muted)}
.service{width:210px;text-align:center}
.service-icon{width:86px;height:86px;margin:0 auto;position:relative}
.service-name{margin-top:20px;font-family:"Poppins",sans-serif;font-weight:600;font-size:14px;color:var(--ink)}
.service-text{margin-top:6px;font-size:12px;line-height:17px;color:var(--text)}
.services-btn{left:536px;top:1231px;width:128px;height:37px}

/* about */
.about-band{left:0;top:1367px;width:1200px;height:431px;background:linear-gradient(120deg,#e3e7ee,#f2f4f7 60%,#e6eaf0)}
.about-title{left:160px;top:1408px;font-family:"Poppins",sans-serif;font-weight:500;font-size:28px;color:var(--ink)}
.about-text{left:160px;top:1470px;width:368px;font-size:12.5px;line-height:20px;color:#444}
.about-text p+p{margin-top:16px}
.about-btn{left:160px;top:1692px;width:128px;height:36px}
.about-visual{left:565px;top:1435px;width:517px;height:271px;background:linear-gradient(180deg,#d7e4f2,#c9d6e6);border-radius:6px}

/* references */
.refs-title{left:464px;width:270px;top:1932px}
.refs-sub{left:464px;width:270px;top:1978px;text-align:center;font-size:15px;color:var(--muted)}
.ref-card{border:8px solid var(--purple)}
.refs-btn{left:534px;top:2454px;width:130px;height:40px}
.divider{left:0;top:2616px;width:1200px;height:1px;background:#e5e5e5}

/* customers */
.customers-title{left:0;width:1200px;top:2668px}
.customers-sub{left:0;width:1200px;top:2714px;text-align:center;font-size:14px;color:var(--muted)}
.client{width:152px;height:84px;border:2px solid var(--purple-soft);background:var(--white);display:flex;align-items:center;justify-content:center;font-family:"PT Sans",sans-serif;font-weight:700;font-size:20px;color:var(--purple);box-shadow:0 3px 8px rgba(0,0,0,.15);z-index:2}

/* footer */
.footer-logo{left:165px;top:3232px;font-family:"Poppins",sans-serif;font-weight:700;font-size:38px;color:var(--purple)}
.footer-text{left:165px;top:3300px;width:370px;font-size:12px;line-height:19px;color:#444}
.socials{left:173px;top:3380px;display:flex;gap:14px}
.socials span{width:22px;height:22px;border-radius:50%;background:#b9b9b9}
.footer-col-title{font-family:"PT Sans",sans-serif;font-size:16px;color:var(--white)}
.quick{left:697px;top:3236px;z-index:2}
.quick ul{list-style:none;margin-top:14px;font-size:12px;line-height:23px;color:#e7def3}
.quick li::before{content:"•";margin-right:14px;color:#e7def3}
.contact{left:875px;top:3236px;z-index:2}
.contact-row{display:flex;align-items:flex-start;gap:12px;margin-top:14px;font-size:12px;line-height:17px;color:#e7def3}
.contact-row svg{flex:none;margin-top:1px}
.footer-line{left:682px;top:3457px;width:480px;height:1px;background:rgba(255,255,255,.3);z-index:2}
.copyright{left:682px;width:480px;top:3477px;text-align:center;font-size:11px;color:#e7def3;z-index:2}
</style>
</head>
<body>

<svg class="bg-shape" width="1200" height="900" viewBox="0 0 1200 900" aria-hidden="true">
  <path d="M0 0H1200V230C1090 240 1020 310 1000 430C980 560 900 620 760 650C600 685 520 700 470 770C420 840 210 820 0 830Z" fill="var(--purple-soft)"/>
  <path d="M0 0H1200V200C1080 215 1010 290 985 410C960 535 880 590 740 620C580 655 500 670 450 735C400 800 200 790 0 800Z" fill="var(--purple)"/>
</svg>

<div class="abs logo">TovanKreativ.de</div>
<nav class="abs nav">
  <span class="active">HOME</span><span>DSGVO</span><span>ABOUT US</span><span>SERVICES</span><span>CREDENTIALS</span><span>CURRENT</span><span>CONTACT</span>
</nav>

<h1 class="abs hero-title">Ideen &amp; Visionen<br>gemeinsam<br>verwirklichen !</h1>
<p class="abs hero-sub">Neue Märkte • Mehr Umsatz • Neue Kunden</p>
<div class="btn hero-btn">Read More</div>
<div class="abs device"><div class="device-screen" role="img" aria-label="Tablet screen showing an SEO gear diagram"></div></div>

<h2 class="abs heading services-title">Our Services</h2>
<p class="abs services-desc">A full service agency is a service company that advises, accompanies, and designs and produces advertising campaigns for other companies in the marketing and advertising sectors.</p>

<div class="abs service" style="left:165px;top:1024px">
  <svg class="service-icon" viewBox="0 0 86 86"><circle cx="43" cy="43" r="40" fill="none" stroke="#ccc" stroke-width="2"/><circle cx="83" cy="43" r="5" fill="var(--purple)"/><circle cx="43" cy="38" r="14" fill="var(--purple)"/><path d="M29 38a14 14 0 0 1 28 0" fill="none" stroke="var(--purple)" stroke-width="3"/><rect x="32" y="52" width="22" height="10" rx="3" fill="var(--purple)"/></svg>
  <div class="service-name">Full Service Agency</div>
  <div class="service-text">A full service agency is a<br>service company that</div>
</div>
<div class="abs service" style="left:377px;top:1024px">
  <svg class="service-icon" viewBox="0 0 86 86"><circle cx="43" cy="43" r="40" fill="none" stroke="#ccc" stroke-width="2"/><circle cx="83" cy="43" r="5" fill="var(--purple)"/><rect x="24" y="28" width="38" height="26" rx="2" fill="none" stroke="var(--purple)" stroke-width="3"/><path d="M36 58h14M43 54v4M38 38l-4 3 4 3M48 38l4 3-4 3" fill="none" stroke="var(--purple)" stroke-width="2.5"/></svg>
  <div class="service-name">Web Development</div>
  <div class="service-text">A full service agency is a<br>service company that</div>
</div>
<div class="abs service" style="left:589px;top:1024px">
  <svg class="service-icon" viewBox="0 0 86 86"><circle cx="43" cy="43" r="40" fill="none" stroke="#ccc" stroke-width="2"/><circle cx="83" cy="43" r="5" fill="var(--purple)"/><rect x="22" y="30" width="32" height="22" rx="2" fill="none" stroke="var(--purple)" stroke-width="3"/><rect x="50" y="36" width="14" height="22" rx="2" fill="#fff" stroke="var(--purple)" stroke-width="3"/><path d="M30 58h16" stroke="var(--purple)" stroke-width="3"/></svg>
  <div class="service-name">Responsive Design</div>
  <div class="service-text">A full service agency is a<br>service company that</div>
</div>
<div class="abs service" style="left:801px;top:1024px">
  <svg class="service-icon" viewBox="0 0 86 86"><circle cx="43" cy="43" r="40" fill="none" stroke="#ccc" stroke-width="2"/><circle cx="83" cy="43" r="5" fill="var(--purple)"/><rect x="24" y="30" width="38" height="24" rx="2" fill="none" stroke="var(--purple)" stroke-width="3"/><path d="M34 60h18M36 48l14-12" stroke="var(--purple)" stroke-width="3"/></svg>
  <div class="service-name">Graphic Design</div>
  <div class="service-text">A full service agency is a<br>service company that</div>
</div>
<div class="btn services-btn">View More</div>

<div class="abs about-band"></div>
<h2 class="abs about-title">ABOUT US</h2>
<div class="abs about-text">
  <p>The advertising agency Tovan Kreativ has existed since 1998. Founded under the name KL-Netzdienst, we have been successfully accompanying your projects on the way to the Internet and the big wide advertising world ever since.</p>
  <p>The advertising agency Tovan Kreativ consists of a team of ambitious programmers, designers and marketing experts full of ideas. With us you get everything from one source: from the design of classic print media on the development of logos and corporate design to the realization of your website or your online store s.</p>
</div>
<div class="btn about-btn">View More</div>
<div class="abs about-visual" role="img" aria-label="Desktop, laptop, tablet and phone showing a responsive website"></div>

<div class="abs ref-card" style="left:160px;top:1930px;width:268px;height:270px;background:linear-gradient(180deg,#c9b9a8,#8a3a3a 55%,#d7d2cc)" role="img" aria-label="Reference website screenshot for a welfare association"></div>
<div class="abs ref-card" style="left:160px;top:2236px;width:268px;height:270px;background:linear-gradient(180deg,#e8efe6,#7fa06e 60%,#d9dcd4)" role="img" aria-label="Reference website screenshot for a transport company"></div>
<h2 class="abs heading refs-title">References</h2>
<p class="abs refs-sub">Small excerpt of our works</p>
<div class="abs ref-card" style="left:464px;top:2033px;width:270px;height:372px;background:linear-gradient(180deg,#dfe7ef,#5e87b5 45%,#c7d3df)" role="img" aria-label="Reference website screenshot for a wholesale company"></div>
<div class="btn refs-btn">View More</div>
<div class="abs ref-card" style="left:770px;top:1930px;width:268px;height:270px;background:linear-gradient(135deg,#f3f1ee,#c8bfb5)" role="img" aria-label="Reference website screenshot for an interior products company"></div>
<div class="abs ref-card" style="left:770px;top:2236px;width:268px;height:270px;background:linear-gradient(180deg,#dfe8f0,#9a4a3c 55%,#6f8a5a)" role="img" aria-label="Reference website screenshot for a farm guesthouse"></div>
<div class="abs divider"></div>

<svg class="bg-shape" width="1200" height="3529" viewBox="0 0 1200 3529" aria-hidden="true" style="z-index:0">
  <path d="M1200 2830C1080 2980 880 2990 760 3100C600 3180 620 3380 520 3440C330 3505 140 3440 0 3480V3529H1200Z" fill="var(--purple-soft)"/>
  <path d="M1200 2870C1090 3010 900 3020 785 3125C580 3200 600 3400 540 3455C350 3520 150 3460 0 3500V3529H1200Z" fill="var(--purple)"/>
</svg>

<h2 class="abs heading customers-title">Our Customers</h2>
<p class="abs customers-sub">Tovan Kreativ and KL-Netzdienst</p>
<div class="abs client" style="left:160px;top:2777px">Nordtal</div>
<div class="abs client" style="left:341px;top:2777px">Bewa</div>
<div class="abs client" style="left:522px;top:2777px">Klarmo</div>
<div class="abs client" style="left:706px;top:2777px">Gerun</div>
<div class="abs client" style="left:885px;top:2777px">Weltek</div>
<div class="abs client" style="left:160px;top:2903px">Falkor</div>
<div class="abs client" style="left:341px;top:2903px">Mertin</div>
<div class="abs client" style="left:522px;top:2903px">Gitra</div>
<div class="abs client" style="left:706px;top:2903px">Paulsen</div>
<div class="abs client" style="left:885px;top:2903px">Sonnhof</div>

<div class="abs footer-logo">TovanKreativ.de</div>
<p class="abs footer-text">A full service agency is a service company that advises, accompanies, and designs and produces advertising campaigns for other companies in the marketing and advertising sectors.</p>
<div class="abs socials"><span></span><span></span><span></span><span></span><span></span><span></span></div>

<div class="abs quick">
  <div class="footer-col-title">Quick Links</div>
  <ul><li>Home</li><li>About Us</li><li>DSGVO</li><li>Services</li><li>Credentials</li><li>Current</li><li>Contact</li></ul>
</div>
<div class="abs contact">
  <div class="footer-col-title">Contact Us</div>
  <div class="contact-row"><svg width="12" height="16" viewBox="0 0 12 16"><path d="M6 0a6 6 0 0 1 6 6c0 4-6 10-6 10S0 10 0 6a6 6 0 0 1 6-6z" fill="#fff"/><circle cx="6" cy="6" r="2.2" fill="var(--purple)"/></svg><span>Lindenweg 14 | 34117 Kassel ,<br>Germany</span></div>
  <div class="contact-row"><svg width="14" height="10" viewBox="0 0 14 10"><rect width="14" height="10" rx="1" fill="#fff"/><path d="M0 1l7 5 7-5" fill="none" stroke="var(--purple)" stroke-width="1.3"/></svg><span>buero@tovankreativ.de</span></div>
  <div class="contact-row"><svg width="14" height="14" viewBox="0 0 14 14"><path d="M3 0l3 3-2 2c1 2 3 4 5 5l2-2 3 3-2 3C6 14 0 8 0 2z" fill="#fff"/></svg><span>0561 - 410 273</span></div>
  <div class="contact-row"><svg width="14" height="14" viewBox="0 0 14 14"><rect x="1" y="4" width="12" height="8" rx="1" fill="#fff"/><rect x="4" y="1" width="6" height="4" fill="#fff"/></svg><span>0561 - 48 19 60</span></div>
</div>
<div class="abs footer-line"></div>
<div class="abs copyright">Copyright 2018 TovanKreativ.de | All Rights Reserved</div>

</body>
</html>
```